Design a Site That Says: ‘This is the Next Big Thing in Defense Tech

We are redesigning the Torvane Aircraft website to deliver a bold, high-impact digital experience that convinces on-the-fence investors this is the moment to get involved. The site must feel fast-moving, technology-forward, and unlike anything coming out of traditional aerospace — no more beige PDFs or outdated defense branding. It should reflect the precision, autonomy, and scale of our product without revealing the proprietary details. Through sleek, modern visuals, sharp messaging, and subtle cues of aerospace innovation — airport runways, carbon fiber textures, night imagery, and mission-ready tone — we want to guide the audience toward one powerful conclusion: Torvane Aircraft is building the future of autonomous defense aviation, and the time to invest is now.
✈️ What Is Torvane Aircraft?
Torvane Aircraft is a next-generation autonomous aerial system built for the future of defense. Where legacy drones were designed for one-off missions and slow production pipelines, Torvane is built from the ground up for speed, scalability, and autonomy. Its sleek, tailless design reflects not just a new aircraft, but a new philosophy: one where performance, flexibility, and manufacturing efficiency converge.

This is not another iteration — it’s a complete rethink of how unmanned systems should be built, deployed, and scaled.

🧩 Competitive Discriminators
1. Production-First Philosophy
Most aircraft are built like custom machines. Torvane is different — it’s engineered for rapid production using cutting-edge methods adapted from high-rate industries. This isn’t just about speed — it’s about being able to respond to demand in real time.

2. Autonomy at the Core
Torvane doesn’t rely on ground crews or remote pilots. It’s built for full autonomy — to operate as a single asset or as part of a larger, coordinated swarm without micromanagement.

3. Modularity Without Compromise
One airframe. Many missions. With a modular internal architecture, Torvane can be adapted to a wide range of operational roles without altering its core structure — or its production rhythm.

4. Clean Configuration, Internal Systems
Everything is housed inside — systems, sensors, payloads — resulting in a streamlined platform that looks and performs differently from the start.

5. Distinct Visual Signature
From its tailless form to its smooth composite surfaces, Torvane Aircraft looks like the future — because it is. It’s what happens when aerospace engineers design without compromise.

👀 What Will Stand Out — Even to a Casual Observer
It doesn’t look like any drone they’ve seen before.
No tail, no hardpoints, no draggy silhouettes — just smooth geometry and silent confidence.

It feels like it belongs to the next generation.
While legacy platforms show their age, Torvane shows what’s next. It looks engineered, not assembled.

It invites imagination.
Observers can’t help but wonder: What’s inside? What can it do? How is it built so differently?

It feels like a system, not just an aircraft.
From design to production to deployment, everything about Torvane is intentional — and scalable.

```html
<!DOCTYPE html>
<html lang="en">
<head>
<meta charset="utf-8">
<title>Torvane Aircraft</title>
<link href="https://fonts.googleapis.com/css2?family=Prompt:wght@400;500&family=Roboto:wght@500&display=swap" rel="stylesheet">
<style>
  :root {
    --ink: #0d0d0d;
    --paper: #ffffff;
    --brand-blue: #0f6fc6;
    --cloud-light: #eef1f5;
    --cloud-mid: #c9d3de;
    --cloud-deep: #8ea2b8;
  }
  * { margin: 0; padding: 0; box-sizing: border-box; }
  html, body { width: 1200px; height: 813px; overflow: hidden; background: var(--paper); }
  body { position: relative; font-family: "Prompt", sans-serif; color: var(--ink); }

  .hero { position: absolute; left: 0; top: 0; width: 1200px; height: 668px; overflow: hidden; }
  .hero-photo {
    position: absolute; left: 0; top: 0; width: 100%; height: 100%;
    background:
      linear-gradient(180deg, var(--paper) 0%, var(--paper) 45%, rgba(255,255,255,0) 70%),
      linear-gradient(180deg, var(--cloud-light) 40%, var(--cloud-mid) 75%, var(--cloud-deep) 100%);
  }

  .site-header { position: absolute; left: 0; top: 0; width: 100%; height: 110px; }
  .brand {
    position: absolute; left: 50%; top: 46px; transform: translateX(-50%);
    display: flex; align-items: center; gap: 8px;
    font-family: "Prompt", sans-serif; font-weight: 500; font-size: 22px;
    letter-spacing: 3px; color: var(--ink); text-transform: uppercase;
  }
  .brand-square { width: 12px; height: 12px; background: var(--brand-blue); }
  .menu-toggle { position: absolute; left: 980px; top: 48px; width: 32px; height: 24px; }

  .hero-content { position: absolute; left: 0; top: 203px; width: 100%; text-align: center; }
  .hero-kicker { font-size: 17px; font-weight: 400; line-height: 28px; }
  .hero-title {
    margin-top: 33px; font-size: 43px; font-weight: 500; line-height: 58px; word-spacing: 4px;
  }
  .hero-cta {
    display: inline-block; margin-top: 50px; width: 128px; height: 33px; line-height: 33px;
    background: var(--brand-blue); color: var(--paper); border-radius: 3px;
    font-family: "Roboto", sans-serif; font-weight: 500; font-size: 15px; text-decoration: none;
  }

  .focus-heading {
    position: absolute; left: 0; top: 748px; width: 100%; text-align: center;
    font-size: 27px; font-weight: 500; line-height: 36px;
  }
</style>
</head>
<body>
  <section class="hero">
    <div class="hero-photo" role="img" aria-label="View from an aircraft window of a jet engine nacelle above a sea of white clouds"></div>

    <header class="site-header">
      <div class="brand"><span class="brand-square"></span>Torvane</div>
      <svg class="menu-toggle" viewBox="0 0 32 24" aria-label="Menu">
        <path d="M4 3 H28 M0 12 H32 M4 21 H28" stroke="#0d0d0d" stroke-width="2.5" stroke-linecap="round"/>
      </svg>
    </header>

    <div class="hero-content">
      <p class="hero-kicker">Enhancing Warfighter Capability, Driving Affordability, Powering Scalable Innovation</p>
      <h1 class="hero-title">Revolutionary Capability,<br>Evolutionary Technology</h1>
      <a class="hero-cta" href="#focuses">Explore More</a>
    </div>
  </section>

  <h2 class="focus-heading" id="focuses">Strategic Innovation Focuses</h2>
</body>
</html>
```